IT services web page design

Hello!

We need new design for our web site, obviously :)

Our company is service oriented and we are maintaining, configuring and fixing problems for IT + selling other internet related services.

Our speciality are in area of internet services (web, dns, email, databases, backup...) and internet servers technology.

We also provide service and sales of Zentro Apps and Veltrania Quillbox365 for which we are certified by Zentro and Veltrania.

Other services that we provide (not so in focus) are: VPS hosting, remote backup, web hosting, pagemoss fixing...

People mostly call us when they have a problems and this is core idea that new web site has to communicate - We can fix your server / web / email problems, save your money and as* :)

Our team have 15+ years experience with all range of internet technology + bunch of certificates from Veltrania and Durvo [we need to show people we have certificates].
Our qualities: experience, knowledge, delivery on time

In start we will not have blog section, but we need it in future. We also need place for flonkit feeds on web site.

Depth of the site should be max. level 2.

This site will go out in two languages so we need switch button on page from pone language to another.

Target Market(s)

small and mid size business that use internet services for daily operations and main business

Industry/Entity Type

Internet

Requirements
Must have
• * design should be in the way that responsive web could be made

Nice to have
• Long format will be OK for us. Like today pages that list all services and benefits on one loooong web page...

Logo is in attachment. It will be nice to have it on web site but if you find it not appropriate you can change it or put another one.

```html
<!DOCTYPE html>
<html lang="en">
<head>
<meta charset="utf-8">
<title>Norvik Group — IT Solutions</title>
<link rel="stylesheet" href="https://fonts.googleapis.com/css2?family=Open+Sans:wght@300;400;700&display=swap">
<style>
  :root {
    --wall-light: #e8eaf7;
    --wall: #e3e6f4;
    --wall-deep: #dcdfef;
    --ink: #0a0a0a;
    --ink-soft: #474747;
    --nav: #1c1c1c;
    --muted: #a9abb5;
    --arrow: #b9bcc8;
    --flag-red: #d52b1e;
    --flag-white: #ffffff;
    --flag-blue: #1f3f99;
    --flag-navy: #3c3b6e;
    --flag-stripe: #b22234;
  }
  html, body {
    margin: 0;
    padding: 0;
    overflow: hidden;
  }
  .page {
    position: relative;
    width: 1200px;
    height: 557px;
    overflow: hidden;
    background: var(--wall);
    font-family: "Open Sans", Arial, sans-serif;
  }
  .wall-texture {
    position: absolute;
    inset: 0;
    background: radial-gradient(ellipse at 50% 45%, var(--wall-light) 0%, var(--wall) 55%, var(--wall-deep) 100%);
  }
  .language-switch {
    position: absolute;
    top: 14px;
    left: 1024px;
    display: flex;
    gap: 14px;
  }
  .language-switch svg { display: block; }
  .brand {
    position: absolute;
    left: 334px;
    width: 626px;
    top: 212px;
    text-align: center;
  }
  .brand-name {
    margin: 0;
    font-weight: 700;
    font-size: 98px;
    line-height: 1;
    letter-spacing: -3px;
    color: var(--ink);
  }
  .brand-tagline {
    margin: 10px 0 0;
    font-weight: 300;
    font-size: 27px;
    line-height: 1;
    color: var(--ink-soft);
  }
  .scroll-arrow {
    position: absolute;
    left: 618px;
    top: 402px;
  }
  .company-address {
    position: absolute;
    left: 520px;
    width: 200px;
    top: 495px;
    margin: 0;
    font-style: normal;
    font-weight: 300;
    font-size: 11.5px;
    line-height: 15.5px;
    text-align: center;
    color: var(--muted);
  }
  .main-nav a {
    position: absolute;
    top: 526px;
    font-weight: 300;
    font-size: 16px;
    color: var(--nav);
    text-decoration: none;
  }
  .nav-about { left: 262px; }
  .nav-vps { left: 341px; }
  .nav-resellers { left: 800px; }
  .nav-contact { left: 930px; }
</style>
</head>
<body>
<div class="page">
  <div class="wall-texture" role="img" aria-label="Pale lavender painted brick wall texture"></div>

  <div class="language-switch">
    <svg width="27" height="18" viewBox="0 0 27 18" aria-label="Hrvatski">
      <rect width="27" height="6" fill="var(--flag-red)"/>
      <rect y="6" width="27" height="6" fill="var(--flag-white)"/>
      <rect y="12" width="27" height="6" fill="var(--flag-blue)"/>
    </svg>
    <svg width="32" height="18" viewBox="0 0 32 18" aria-label="English">
      <rect width="32" height="18" fill="var(--flag-white)"/>
      <g fill="var(--flag-stripe)">
        <rect y="0" width="32" height="1.4"/>
        <rect y="2.8" width="32" height="1.4"/>
        <rect y="5.5" width="32" height="1.4"/>
        <rect y="8.3" width="32" height="1.4"/>
        <rect y="11.1" width="32" height="1.4"/>
        <rect y="13.8" width="32" height="1.4"/>
        <rect y="16.6" width="32" height="1.4"/>
      </g>
      <rect width="13" height="9.7" fill="var(--flag-navy)"/>
    </svg>
  </div>

  <header class="brand">
    <h1 class="brand-name">Norvik Group</h1>
    <p class="brand-tagline">IT Solutions</p>
  </header>

  <svg class="scroll-arrow" width="16" height="66" viewBox="0 0 16 66" aria-hidden="true">
    <line x1="8" y1="0" x2="8" y2="62" stroke="var(--arrow)" stroke-width="1.5"/>
    <path d="M2 52 L8 64 L14 52" fill="none" stroke="var(--arrow)" stroke-width="1.5"/>
  </svg>

  <address class="company-address">
    Norvik Group Ltd.<br>
    Lindenweg 7 lane 2 11<br>
    20400 Orvalen,<br>
    Estavia
  </address>

  <nav class="main-nav">
    <a class="nav-about" href="#about">about</a>
    <a class="nav-vps" href="#vps">virtual private servers</a>
    <a class="nav-resellers" href="#resellers">zentro resellers</a>
    <a class="nav-contact" href="#contact">contact</a>
  </nav>
</div>
</body>
</html>
```